Website design for Keystone Stewardship Australia, a new boutique specialist consultancy company

We need a web design for a new company based in Australia called Keystone Stewardship Australia (this is abbreviated in our logo to KSA).

KSA is a boutique specialist advisory firm that provides Interim Management and Executive Transition Services. Through a suite of best practice methodologies coupled with advisory and consulting services, KSA supports businesses and executives during times of leadership hiatus and transition which not only mitigates risk of transition failure, but more importantly accelerates transition success.

Delphine at PixelHarbor has designed our logo (see attached file) and the logo and its colours will guide the website design. The primary colour scheme will be in the turquoise/aqua range and may include accent colours - designer's creative choice and guidance is welcome here.

The website should convey an image of crisp, modern professionalism. It's purpose will be to provide information about the company, our products and services and provide contact details. There is no online ordering or payment functionality required. Pages will include a home page with general information about the company, a number of content pages outlining information about each aspect of the services offered, an "about us" page and a "contact us" page.

Target Market(s)

This is a Busines-to-Business company and our target market is primarily large and medium sized companies. The specific individuals targeted at these companies will include:

Human Resources Directors
Talent and Recruitment Heads
Boards and Senior Executive teams of companies
Hiring managers responsible for recruiting and managing senior leaders and executives

Industry/Entity Type

Boutique

Requirements
Should not have
• Online ordering / payment page

```html
<!DOCTYPE html>
<html lang="en">
<head>
<meta charset="utf-8">
<title>Keystone Stewardship Australia</title>
<link rel="stylesheet" href="https://fonts.googleapis.com/css2?family=Open+Sans:ital,wght@0,300;0,400;0,600;0,700;1,400&display=swap">
<style>
:root{
  --primary:#1aa6b0;
  --primary-dark:#12828b;
  --accent:#e8511f;
  --ink:#1e1e1e;
  --body:#555;
  --muted:#777;
  --light:#f4f4f4;
  --white:#fff;
}
*{margin:0;padding:0;box-sizing:border-box}
html,body{width:1200px;height:3499px;overflow:hidden}
body{font-family:"Open Sans",Arial,sans-serif;color:var(--ink);background:var(--white);position:relative}
section,header,footer{position:absolute;left:0;width:1200px}
.section-title{position:absolute;left:0;width:100%;text-align:center;font-weight:400;font-size:56px;letter-spacing:-1px;color:var(--ink)}
.section-intro{position:absolute;left:300px;width:600px;text-align:center;font-size:14px;line-height:21px;color:var(--muted)}

/* Hero */
.hero{top:0;height:683px;background:linear-gradient(160deg,#9a9a9a 0%,#5b5b5b 35%,#7d7d7d 60%,#3c3c3c 100%);overflow:hidden}
.hero-photo{position:absolute;inset:0;background:radial-gradient(ellipse at 55% 40%,rgba(220,220,220,.35),rgba(0,0,0,.25) 70%)}
.brand{position:absolute;left:18px;top:14px;width:420px;height:130px;background:var(--white);display:flex;align-items:center;padding-left:22px;gap:16px}
.brand-mark{font-weight:700;font-size:56px;color:var(--primary);letter-spacing:-1px}
.brand-name{font-weight:700;font-size:22px;line-height:27px;color:var(--primary)}
.main-nav{position:absolute;left:525px;top:18px;width:675px;height:88px;background:var(--primary);display:flex;align-items:center;padding-left:28px;gap:56px}
.main-nav a{color:var(--white);text-decoration:none;font-size:22px;font-weight:400}
.hero-title{position:absolute;top:210px;width:100%;text-align:center;color:var(--white);font-size:50px;font-weight:300;letter-spacing:1px}
.hero-lead{position:absolute;top:288px;width:100%;text-align:center;color:#f0f0f0;font-size:17px;line-height:25px}
.play{position:absolute;left:570px;top:375px}
.hero-note{position:absolute;top:468px;width:100%;text-align:center;color:#e8e8e8;font-size:16px;line-height:24px}
.btn-showroom{position:absolute;left:460px;top:566px;width:280px;height:44px;background:var(--accent);color:var(--white);font-size:19px;text-align:center;line-height:44px;text-decoration:none}

/* Services */
.services{top:683px;height:584px;background:var(--white)}
.services .section-title{top:60px}
.services .section-intro{top:140px}
.service{position:absolute;top:270px;width:270px;text-align:center}
.service-icon{display:block;margin:0 auto}
.service h3{font-size:26px;font-weight:700;margin-top:24px}
.service p{font-size:13px;line-height:17px;color:var(--body);margin-top:6px;padding:0 6px}
.read-more{display:block;text-align:left;margin:10px 0 0 28px;font-size:15px;color:var(--ink);text-decoration:none}

/* About */
.about{top:1267px;height:571px;background:var(--light)}
.about .section-title{top:50px}
.about .section-intro{top:130px}
.about-device{position:absolute;left:168px;top:246px;width:304px;height:240px;background:linear-gradient(180deg,#2a2a2a 0%,#444 78%,#cfcfcf 78%,#e6e6e6 100%);border-radius:8px}
.about-copy{position:absolute;left:490px;top:245px;width:665px}
.about-copy h3{font-size:30px;font-weight:400;color:var(--ink)}
.about-copy .lead{font-family:"Times New Roman",Georgia,serif;font-style:italic;font-size:18px;line-height:22px;color:#222;margin-top:12px}
.about-copy .body{font-size:15px;line-height:20px;color:var(--body);margin-top:12px;text-align:justify}
.about-copy .read-more{margin:16px 0 0;color:var(--accent);font-size:15px}

/* Portfolio */
.portfolio{top:1838px;height:682px;background:var(--primary)}
.portfolio .section-title{top:50px}
.portfolio .section-intro{top:130px;color:#0b3f43}
.portfolio-grid{position:absolute;left:203px;top:227px;width:795px;height:403px;display:grid;grid-template-columns:repeat(3,1fr);grid-template-rows:repeat(2,1fr)}
.work{position:relative}
.work-a{background:linear-gradient(180deg,#f4f4f4,#e6e6e6)}
.work-b{background:#ececec}
.work-c{background:#2f2f2f}
.work-d{background:#f6f6f6}
.work-e{background:var(--primary-dark)}
.work-f{background:#fbfbfb}
.work-label{position:absolute;left:0;bottom:52px;width:100%;height:44px;background:rgba(232,81,31,.88);color:var(--white);font-size:26px;line-height:44px;padding-left:20px}
.arrow{position:absolute;top:402px}

/* Crew */
.crew{top:2520px;height:700px;background:var(--white)}
.crew .section-title{top:55px}
.crew .section-intro{top:135px;width:560px;left:320px}
.member{position:absolute;top:250px;width:280px;text-align:center}
.member-photo{width:200px;height:200px;border-radius:50%;margin:0 auto;background:linear-gradient(160deg,#d9d4cf,#8d8074)}
.member h3{font-weight:400;font-size:24px;color:var(--primary);margin-top:46px}
.member p{font-size:13px;line-height:17px;color:var(--body);margin-top:8px;padding:0 22px}

/* Footer */
.site-footer{top:3220px;height:245px;background:var(--primary)}
.footer-col{position:absolute;top:34px;width:190px}
.footer-col h4{color:var(--white);font-weight:400;font-size:26px;line-height:34px}
.footer-col ul{list-style:none;margin-top:10px}
.footer-col li{font-size:13px;color:var(--white);height:31px;line-height:31px;border-bottom:1px solid rgba(255,255,255,.3);white-space:nowrap}
.legal{position:absolute;left:0;top:3465px;width:1200px;height:34px;background:var(--white);font-size:13px;line-height:34px;padding-left:172px;color:var(--ink)}
.legal strong{color:var(--primary)}
</style>
</head>
<body>

<header class="hero">
  <div class="hero-photo" role="img" aria-label="Black and white aerial photograph of a city skyline"></div>
  <div class="brand">
    <span class="brand-mark">KSA</span>
    <span class="brand-name">Keystone Stewardship<br>Australia Pty Ltd</span>
  </div>
  <nav class="main-nav">
    <a href="#">HOME</a><a href="#">ABOUT US</a><a href="#">SERVICES</a><a href="#">CONTACT</a>
  </nav>
  <h1 class="hero-title">INCREDIBILE SERVICE</h1>
  <p class="hero-lead">Discover how our process brings everything you need to<br>lead with confidence and take the steps that deliver.</p>
  <svg class="play" width="60" height="60" viewBox="0 0 60 60" aria-hidden="true">
    <circle cx="30" cy="30" r="27" fill="none" stroke="#fff" stroke-width="3"/>
    <path d="M24 18 L42 30 L24 42 Z" fill="#fff"/>
  </svg>
  <p class="hero-note">Start your journey in minutes<br>Watch our short film</p>
  <a class="btn-showroom" href="#">VISIT OUR SHOWROOM!</a>
</header>

<section class="services">
  <h2 class="section-title">OUR SERVICES</h2>
  <p class="section-intro">Search for anything people, topics, hashtags, your favorite sites and then flip through articles, updates, photos and videos all in a beautiful magazine-style format.</p>

  <div class="service" style="left:155px">
    <svg class="service-icon" width="104" height="104" viewBox="0 0 104 104" aria-hidden="true">
      <circle cx="52" cy="52" r="52" fill="var(--primary)"/>
      <rect x="31" y="31" width="42" height="42" fill="none" stroke="#fff" stroke-width="3"/>
      <rect x="37" y="56" width="6" height="13" fill="#fff"/>
      <rect x="47" y="50" width="6" height="19" fill="#fff"/>
      <rect x="57" y="43" width="6" height="26" fill="#fff"/>
      <path d="M36 50 L48 42 L56 46 L68 35" stroke="#fff" stroke-width="3" fill="none"/>
    </svg>
    <h3>Lorem ipsum</h3>
    <p>Lorem ipsum dolor sit amet, consectetuer adipiscing elit, sed diam ut laoreet dolore magna volutpat.</p>
    <a class="read-more" href="#">&gt;&gt; READ MORE</a>
  </div>

  <div class="service" style="left:460px">
    <svg class="service-icon" width="104" height="104" viewBox="0 0 104 104" aria-hidden="true">
      <circle cx="52" cy="52" r="52" fill="var(--primary)"/>
      <path d="M50 30 A22 22 0 1 0 72 52 L50 52 Z" fill="#fff"/>
      <path d="M55 26 A22 22 0 0 1 76 47 L55 47 Z" fill="#fff"/>
    </svg>
    <h3>Lorem ipsum</h3>
    <p>Lorem ipsum dolor sit amet, consectetuer adipiscing elit, sed diam ut laoreet dolore magna volutpat.</p>
    <a class="read-more" href="#">&gt;&gt; READ MORE</a>
  </div>

  <div class="service" style="left:765px">
    <svg class="service-icon" width="104" height="104" viewBox="0 0 104 104" aria-hidden="true">
      <circle cx="52" cy="52" r="52" fill="var(--primary)"/>
      <circle cx="52" cy="56" r="21" fill="none" stroke="#fff" stroke-width="3.5"/>
      <rect x="47" y="26" width="10" height="6" fill="#fff"/>
      <path d="M52 56 L52 43 M52 56 L61 61" stroke="#fff" stroke-width="3" stroke-linecap="round"/>
      <path d="M70 34 L74 38" stroke="#fff" stroke-width="3.5" stroke-linecap="round"/>
    </svg>
    <h3>Lorem ipsum</h3>
    <p>Lorem ipsum dolor sit amet, consectetuer adipiscing elit, sed diam ut laoreet dolore magna volutpat.</p>
    <a class="read-more" href="#">&gt;&gt; READ MORE</a>
  </div>
</section>

<section class="about">
  <h2 class="section-title">LET'S TALK ABOUT US</h2>
  <p class="section-intro">Search for anything people, topics, hashtags, your favorite sites and then flip through articles, updates, photos and videos all in a beautiful magazine-style format.</p>
  <div class="about-device" role="img" aria-label="Desktop monitor showing the company name on screen"></div>
  <div class="about-copy">
    <h3>Good solutions for your business!</h3>
    <p class="lead">Lorem ipsum dolor sit amet, consectetuer adipiscing elit, sed diam nonummy nibh euismod tincidunt ut laoreet dolore magna aliquam erat volutpat. Ut wisi enim ad minim veniam.</p>
    <p class="body">Lorem ipsum dolor sit amet, consectetuer adipiscing elit, sed diam nonummy nibh euismod tincidunt ut laoreet dolore magna aliquam erat volutpat. Ut wisi enim ad minim veniam, quis nostrud exerci tation ullamcorper suscipit lobortis nisl ut aliquip ex ea commodo consequat. Duis autem vel eum iriure dolor in hendrerit in vulputate velit esse.</p>
    <a class="read-more" href="#">READ MORE &gt;</a>
  </div>
</section>

<section class="portfolio">
  <h2 class="section-title">OUR PORTFOLIO</h2>
  <p class="section-intro">Search for anything people, topics, hashtags, your favorite sites and then flip through articles, updates, photos and videos all in a beautiful magazine-style format.</p>
  <svg class="arrow" style="left:62px" width="50" height="50" viewBox="0 0 50 50" aria-hidden="true">
    <circle cx="25" cy="25" r="22" fill="none" stroke="#fff" stroke-width="3"/>
    <path d="M29 15 L19 25 L29 35" fill="none" stroke="#fff" stroke-width="3.5"/>
  </svg>
  <div class="portfolio-grid">
    <div class="work work-a" role="img" aria-label="Logo design sample for a sports care clinic"><span class="work-label">LOGO DESIGN</span></div>
    <div class="work work-b" role="img" aria-label="Logo design sample for a record label"></div>
    <div class="work work-c" role="img" aria-label="Logo design sample with a circular emblem on dark grey"></div>
    <div class="work work-d" role="img" aria-label="Logo design sample with a leaf-shaped mark"></div>
    <div class="work work-e" role="img" aria-label="Logo design sample with a geometric shield on teal"></div>
    <div class="work work-f" role="img" aria-label="Logo design sample with an ornate crest"></div>
  </div>
  <svg class="arrow" style="left:1088px" width="50" height="50" viewBox="0 0 50 50" aria-hidden="true">
    <circle cx="25" cy="25" r="22" fill="none" stroke="#fff" stroke-width="3"/>
    <path d="M21 15 L31 25 L21 35" fill="none" stroke="#fff" stroke-width="3.5"/>
  </svg>
</section>

<section class="crew">
  <h2 class="section-title">MEET THE CREW</h2>
  <p class="section-intro">Lorem ipsum dolor sit amet, consectetuer adipiscing elit, sed diam nonummy nibh euismod tincidunt ut laoreet dolore magna aliquam erat volutpat.</p>
  <div class="member" style="left:122px">
    <div class="member-photo" role="img" aria-label="Portrait photograph of a team member"></div>
    <h3>Noah Brenner</h3>
    <p>Lorem ipsum dolor sit amet, consectetuer adipiscing elit, sed diam nonummy nibh euismod tincidunt ut laoreet dolore magna.</p>
  </div>
  <div class="member" style="left:455px">
    <div class="member-photo" role="img" aria-label="Portrait photograph of a team member"></div>
    <h3>Clara Whitfield</h3>
    <p>Lorem ipsum dolor sit amet, consectetuer adipiscing elit, sed diam nonummy nibh euismod tincidunt ut laoreet dolore magna.</p>
  </div>
  <div class="member" style="left:788px">
    <div class="member-photo" role="img" aria-label="Portrait photograph of a team member"></div>
    <h3>Ella Marsh</h3>
    <p>Lorem ipsum dolor sit amet, consectetuer adipiscing elit, sed diam nonummy nibh euismod tincidunt ut laoreet dolore magna.</p>
  </div>
</section>

<footer class="site-footer">
  <div class="footer-col" style="left:158px">
    <h4>ABOUT</h4>
    <ul><li>About Us</li><li>Our Approach</li><li>Privacy Policy</li><li>Terms &amp; Conditions</li><li>Careers</li></ul>
  </div>
  <div class="footer-col" style="left:397px">
    <h4>SERVICES</h4>
    <ul><li>Interim Management</li><li>Executive Transition</li><li>Advisory</li><li>Consulting</li><li>Methodologies</li></ul>
  </div>
  <div class="footer-col" style="left:640px">
    <h4>FOLLOW US</h4>
    <ul><li>News Feed</li><li>Updates</li><li>Gallery</li><li>Videos</li><li>Pinboard</li></ul>
  </div>
  <div class="footer-col" style="left:882px">
    <h4>CONTACT</h4>
    <ul><li>Contact</li><li>Newsletter</li></ul>
  </div>
</footer>
<p class="legal">© <strong>KSA</strong> 2012-2015 ALL RIGHTS RESERVED</p>

</body>
</html>
```